Varnell Skyworks Limited

Started a consulting business 12 months ago and have since moved location and have grown and seek to identify my self to the industry.
Specializing in quality solutions, business documentation and maintenance solution's

Industry/Entity Type

Business

```html
<!DOCTYPE html>
<html lang="en">
<head>
<meta charset="UTF-8">
<title>Varnell Skyworks Limited – Business Card</title>
<link rel="stylesheet" href="https://fonts.googleapis.com/css2?family=Comfortaa:wght@700&family=Michroma&display=swap">
<style>
  :root {
    --bg: #e4e4e2;
    --card-white: #ffffff;
    --card-fade: #ececec;
    --card-black: #232323;
    --accent-green: #9fcb3b;
    --ink: #1c1c1c;
    --text-light: #f2f2f2;
    --text-muted: #d6d6d6;
  }
  * { margin: 0; padding: 0; box-sizing: border-box; }
  html, body {
    width: 1200px; height: 901px; overflow: hidden;
    background: var(--bg);
  }
  .canvas {
    position: relative; width: 1200px; height: 901px;
    display: flex; align-items: center; justify-content: center;
  }
  .card {
    position: relative; width: 900px; height: 514px;
    border-radius: 46px; overflow: hidden;
    background: linear-gradient(180deg, var(--card-white) 0%, var(--card-fade) 55%);
    box-shadow: 0 14px 34px rgba(0,0,0,0.18);
  }
  .card-shapes { position: absolute; inset: 0; }
  .company-name {
    position: absolute; top: 96px; left: 165px;
    font-family: "Comfortaa", sans-serif; font-weight: 700;
    font-size: 46px; letter-spacing: -0.5px; color: var(--ink);
    white-space: nowrap;
  }
  .identity {
    position: absolute; top: 336px; right: 478px;
    text-align: right; font-family: "Michroma", sans-serif;
    color: var(--text-light); text-transform: uppercase;
  }
  .identity .person-name { font-size: 16px; letter-spacing: 2px; margin-bottom: 10px; }
  .identity .person-role { font-size: 12px; letter-spacing: 2px; color: var(--text-muted); margin-bottom: 14px; }
  .identity .address { font-size: 12px; letter-spacing: 1.6px; line-height: 25px; color: var(--text-muted); }
  .divider {
    position: absolute; left: 448px; top: 330px; width: 1.5px; height: 148px;
    background: var(--text-muted);
  }
  .contacts {
    position: absolute; top: 336px; left: 466px;
    list-style: none; font-family: "Michroma", sans-serif;
    font-size: 12.5px; letter-spacing: 1.6px; color: var(--text-light);
  }
  .contacts li { display: flex; align-items: center; gap: 8px; height: 24px; white-space: nowrap; }
  .contacts li.gap-before { margin-top: 8px; }
  .contacts .web { text-transform: lowercase; }
  .contacts svg { width: 15px; height: 15px; flex: none; }
</style>
</head>
<body>
<main class="canvas">
  <section class="card" aria-label="Varnell Skyworks Limited business card">
    <svg class="card-shapes" viewBox="0 0 900 514" preserveAspectRatio="none" aria-hidden="true">
      <path class="dark-base" fill="var(--card-black)"
            d="M0,200 C250,230 450,250 600,285 C740,318 840,380 900,440 L900,514 L0,514 Z"/>
      <path class="green-swoosh" fill="var(--accent-green)"
            d="M0,174 C250,206 450,226 600,260 C740,292 840,354 900,418 L900,432 C840,370 740,308 600,274 C450,242 250,222 0,190 Z"/>
    </svg>

    <h1 class="company-name">Varnell Skyworks Limited</h1>

    <div class="identity">
      <p class="person-name">Elena Marsh</p>
      <p class="person-role">Owner / C.E.O</p>
      <p class="address">Suite # 118, Kestrel Bldg,<br>NY 10472</p>
    </div>

    <div class="divider"></div>

    <ul class="contacts">
      <li>
        <svg viewBox="0 0 16 16"><circle cx="8" cy="8" r="8" fill="var(--text-light)"/><path d="M5 4.5l1.6-.4 1 2.2-1 .8a5 5 0 0 0 2.3 2.3l.8-1 2.2 1-.4 1.6C8 11.5 4.5 8 5 4.5z" fill="var(--card-black)"/></svg>
        555-210-4417
      </li>
      <li>
        <svg viewBox="0 0 16 16"><circle cx="8" cy="8" r="8" fill="var(--text-light)"/><rect x="5.5" y="3.5" width="5" height="9" rx="1" fill="var(--card-black)"/><rect x="6.5" y="5" width="3" height="5" fill="var(--text-light)"/></svg>
        555-638-9052
      </li>
      <li>
        <svg viewBox="0 0 16 16"><circle cx="8" cy="8" r="8" fill="var(--text-light)"/><rect x="4" y="6.5" width="8" height="5" rx="1" fill="var(--card-black)"/><rect x="5.5" y="3.5" width="5" height="3" fill="var(--card-black)"/></svg>
        555-874-2316
      </li>
      <li class="gap-before">
        <svg viewBox="0 0 16 16"><circle cx="8" cy="8" r="8" fill="var(--text-light)"/><rect x="3.8" y="5" width="8.4" height="6" fill="var(--card-black)"/><path d="M3.8 5l4.2 3.4L12.2 5" fill="none" stroke="var(--text-light)" stroke-width="0.9"/></svg>
        <span class="web">elena@varnellsky.com</span>
      </li>
      <li>
        <svg viewBox="0 0 16 16"><circle cx="8" cy="8" r="8" fill="var(--text-light)"/><g fill="none" stroke="var(--card-black)" stroke-width="1"><circle cx="8" cy="8" r="4.5"/><ellipse cx="8" cy="8" rx="2" ry="4.5"/><path d="M3.5 8h9"/></g></svg>
        <span class="web">www.varnellsky.com</span>
      </li>
    </ul>
  </section>
</main>
</body>
</html>
```